Revamp PowerPoint deck to match our new website's visual identity and effectively tell our story

Revamp PowerPoint Deck to Match New Corporate Website Theme @ https://velrisdemo4.xq-stage.net/.
(Note: The content on the new theme is placeholder text. The current live website is www.tovalinfo.net )

Key Request: Slide Master SHOULD NOT include any specific contents. It should contain only essential elements such master layout, the logo, header, footer, and any repeating text elements and it should be limited to a maximum of 5 pages.

We need to redesign our existing PowerPoint deck to align with the visual identity of our new corporate website while ensuring it effectively tells our story. The revamped deck should focus on:

1. Visual Storytelling: Each slide should guide the audience through a clear and compelling narrative. Build on each slide to ensure the story flows seamlessly.

2. Minimal Text, More Visuals: Avoid text-heavy slides. Where text is necessary, keep it concise. Focus on strong visuals, icons, and imagery that reinforce key points. Ensure the visuals are impactful and align with our brand identity. Use bold icons and high-quality images that match the tone of the new website to emphasize key messages.

3. Design Consistency: Ensure the presentation reflects the color palette, typography, and imagery from the new website. This includes maintaining consistency in the style of headings, subheadings, and body text to reinforce our brand identity.

4. Modern & Clean Design: Embrace a minimalist design aesthetic inspired by the new website. Use the same color schemes, fonts, and clean layouts to ensure the slides are visually engaging and easy to digest.

5. Professional, Minimalist Look: Keep the design professional and minimalist, with a focus on clarity. Ensure each slide conveys its message clearly without unnecessary distractions.

Our goal is to create a visually engaging and interactive presentation that clearly communicates our message while keeping the audience engaged.

Ensure our corporate color scheme is maintained as per the current website: www.tovalinfo.net

Target Market(s)

B2B Clients in Asia Pacific and Australia

Industry/Entity Type

Across all industries, but more specific to IT

Requirements
Must have
• nsure our corporate color scheme is maintained as per the current website: www.tovalinfo.net
Nice to have
• More graphics and illustrations than text. Icon representations.
Should not have
• Slide Master SHOULD NOT include any specific contents. It should contain only essential elements such master layout, the logo, header, footer, and any repeating text elements and it should be limited to a maximum of 5 pages

```html
<!DOCTYPE html>
<html lang="en">
<head>
<meta charset="utf-8">
<title>Our Solutions</title>
<link href="https://fonts.googleapis.com/css2?family=Montserrat:wght@800&family=Arimo:wght@700&display=swap" rel="stylesheet">
<style>
  :root {
    --ink: #111111;
    --slate: #4b5671;
    --tile: #5d6a84;
    --rule-grey: #8a8f99;
    --brand-red: #d23a34;
    --paper: #ffffff;
  }
  * { margin: 0; padding: 0; box-sizing: border-box; }
  html, body { width: 1200px; height: 675px; overflow: hidden; background: var(--paper); }
  .slide { position: relative; width: 1200px; height: 675px; overflow: hidden; background: var(--paper); }

  .slide-title {
    position: absolute; left: 48px; top: 20px;
    font-family: "Montserrat", sans-serif; font-weight: 800;
    font-size: 35px; letter-spacing: 0.2px; color: var(--slate);
  }
  .header-rule { position: absolute; left: 0; top: 65px; width: 1200px; height: 2px; background: var(--rule-grey); }

  .frame { position: absolute; width: 145px; height: 144px; border: 2px dashed var(--brand-red); }
  .frame.top { border-bottom: 2px dashed var(--brand-red); }
  .icon-tile {
    position: absolute; width: 84px; height: 84px; background: var(--tile);
    display: flex; align-items: center; justify-content: center;
  }
  .icon-tile svg { width: 46px; height: 46px; fill: none; stroke: #fff; stroke-width: 1.6; stroke-linecap: round; stroke-linejoin: round; }

  .label {
    position: absolute; font-family: "Arimo", sans-serif; font-weight: 700;
    font-size: 16px; line-height: 21px; color: var(--ink);
  }

  .deco { position: absolute; }
  .deco.red { background: var(--brand-red); }
  .deco.grey { background: var(--tile); }

  .footer-rule { position: absolute; left: 0; top: 603px; width: 1200px; height: 5px; background: var(--brand-red); }
  .footer-rule-shadow { position: absolute; left: 0; top: 608px; width: 1200px; height: 2px; background: #e9b3b0; }

  .brand {
    position: absolute; right: 24px; top: 632px;
    display: flex; align-items: center; gap: 8px;
  }
  .brand-name {
    font-family: "Arimo", sans-serif; font-weight: 700; font-size: 24px;
    letter-spacing: 3px; color: var(--brand-red);
  }
  .brand-mark { width: 8px; height: 8px; background: var(--brand-red); }
</style>
</head>
<body>
<main class="slide">
  <h1 class="slide-title">OUR SOLUTIONS</h1>
  <div class="header-rule"></div>

  <!-- top row frames -->
  <div class="frame" style="left:100px; top:184px;"></div>
  <div class="frame" style="left:389px; top:184px;"></div>
  <div class="frame" style="left:676px; top:180px;"></div>
  <div class="frame" style="left:966px; top:177px;"></div>

  <!-- bottom row frames -->
  <div class="frame" style="left:246px; top:328px;"></div>
  <div class="frame" style="left:533px; top:328px;"></div>
  <div class="frame" style="left:824px; top:328px;"></div>

  <!-- icon tiles -->
  <div class="icon-tile" style="left:131px; top:212px;">
    <svg viewBox="0 0 48 48"><path d="M8 18h32l-11 12v8l-10 4V30z"/><circle cx="27" cy="28" r="6"/><circle cx="27" cy="28" r="2"/><path d="M14 12V6M24 12V4M34 12V6"/><circle cx="14" cy="5" r="1.5"/><circle cx="34" cy="5" r="1.5"/></svg>
  </div>
  <div class="icon-tile" style="left:277px; top:357px;">
    <svg viewBox="0 0 48 48"><rect x="14" y="14" width="26" height="9" rx="1"/><rect x="14" y="27" width="26" height="9" rx="1"/><path d="M34 18.5h2M34 31.5h2M27 36v6M18 42h18"/><circle cx="11" cy="12" r="4"/><path d="M11 5v3M11 16v3M4 12h3M15 12h3"/></svg>
  </div>
  <div class="icon-tile" style="left:420px; top:212px;">
    <svg viewBox="0 0 48 48"><rect x="26" y="8" width="16" height="12" rx="1"/><path d="M31 8V5h6v3M26 13h16"/><rect x="6" y="26" width="16" height="12" rx="1"/><path d="M11 26v-3h6v3M6 31h16"/><path d="M20 13h-8v6M9 16l3 3 3-3M28 35h8v-6M33 32l3-3 3 3"/></svg>
  </div>
  <div class="icon-tile" style="left:563px; top:357px;">
    <svg viewBox="0 0 48 48"><rect x="10" y="6" width="24" height="32" rx="1"/><path d="M14 13l2 2 3-3M22 14h8M14 21l2 2 3-3M22 22h8M14 29l2 2 3-3M22 30h4"/><circle cx="36" cy="33" r="4"/><path d="M29 44c0-4 3-6 7-6s7 2 7 6"/></svg>
  </div>
  <div class="icon-tile" style="left:707px; top:212px;">
    <svg viewBox="0 0 48 48"><ellipse cx="18" cy="16" rx="10" ry="4"/><path d="M8 16v14c0 2 4 4 10 4s10-2 10-4V16M8 23c0 2 4 4 10 4s10-2 10-4"/><circle cx="28" cy="26" r="5"/><path d="M33 26h6M28 21V9M31 22l6-8M31 30l6 6M28 31v8"/><circle cx="41" cy="26" r="1.5"/><circle cx="28" cy="8" r="1.5"/><circle cx="38" cy="13" r="1.5"/><circle cx="38" cy="37" r="1.5"/></svg>
  </div>
  <div class="icon-tile" style="left:855px; top:357px;">
    <svg viewBox="0 0 48 48"><rect x="8" y="6" width="22" height="34" rx="1"/><path d="M12 12h14M12 17h14M12 22h10M12 27h10"/><rect x="24" y="22" width="16" height="20" rx="1"/><path d="M28 27h8M28 32h8M28 37h8M32 27v10"/></svg>
  </div>
  <div class="icon-tile" style="left:998px; top:209px;">
    <svg viewBox="0 0 48 48"><rect x="6" y="8" width="36" height="26" rx="1"/><path d="M20 34l-2 6h12l-2-6M14 40h20"/><circle cx="16" cy="18" r="5"/><path d="M11 18h10M16 13c-2 3-2 7 0 10M16 13c2 3 2 7 0 10"/><path d="M26 20l8-5v13l-8-5zM26 20v3M30 25l1 4"/></svg>
  </div>

  <!-- labels -->
  <p class="label" style="left:106px; top:353px;">Effective<br>Multi-channel<br>demand<br>generation</p>
  <p class="label" style="left:259px; top:255px;">Data<br>Management</p>
  <p class="label" style="left:404px; top:353px;">B2B Contact<br>data<br>acquisition</p>
  <p class="label" style="left:548px; top:245px;">Attendees<br>Generation<br>for events</p>
  <p class="label" style="left:694px; top:351px;">Business<br>process<br>outsourcing/<br>CX solutions</p>
  <p class="label" style="left:848px; top:258px;">Account<br>Profiling</p>
  <p class="label" style="left:995px; top:349px;">Digital<br>Marketing</p>

  <!-- corner accent squares -->
  <div class="deco red" style="left:1109px; top:473px; width:25px; height:25px;"></div>
  <div class="deco grey" style="left:1141px; top:498px; width:35px; height:35px;"></div>
  <div class="deco grey" style="left:1099px; top:526px; width:35px; height:35px;"></div>
  <div class="deco red" style="left:1141px; top:531px; width:57px; height:72px;"></div>

  <div class="footer-rule"></div>
  <div class="footer-rule-shadow"></div>

  <div class="brand">
    <span class="brand-name">TOVALINFO</span>
    <span class="brand-mark"></span>
  </div>
</main>
</body>
</html>
```